Business card design for crowd sourced review site.

I need a business card magnet design for an online, crowd-sourced, restaurant review site strictly for Kosher restaurants.
It is similar to RoamLedger but catering to a very particular crowd.
The markets it will be distributed in are flooded with business card fridge magnets so this needs to be eye-catching and unique. The Business name is PlateMarks
The website isnt finished but you can see the basic setup here
http://restaurant.vintrello.com/

The second image i included is another logo design I liked and was thinking about using and decided I will probably also make a SECOND custom cut business card in the shape of that icon. Bonus if you can throw that in also.

Target Market(s)

Jewish consumers aged 20-35

Industry/Entity Type

Business

Contact Information for Business Card

see description.
Design should not be too crowded and should in eye-catching. Will mainly be used as fridge magnets.

Requirements
Must have
• Website address. logo.
Nice to have
• tagline. (The Definitive guide to kosher dining for the Kosher consumer)
• Im not a professional but I personally think the color blue goes along with this concept. ill leave it to you to decide.
Should not have
• any religious symbols.

```html
<!DOCTYPE html>
<html lang="en">
<head>
<meta charset="utf-8">
<title>PlateMarks Business Card</title>
<link href="https://fonts.googleapis.com/css2?family=Open+Sans:wght@400;600&display=swap" rel="stylesheet">
<style>
  :root {
    --page-bg: #e9e6e1;
    --card-black: #050505;
    --accent-red: #e0301e;
    --accent-red-deep: #b8200f;
    --text-white: #ffffff;
    --text-soft: #e6e6e6;
    --grill-dark: #1a1410;
    --grill-mid: #3a2a20;
  }
  * { box-sizing: border-box; margin: 0; padding: 0; }
  html, body {
    width: 1200px; height: 780px; overflow: hidden;
    background: var(--page-bg);
    font-family: "Open Sans", Arial, sans-serif;
  }
  .sheet {
    position: relative; width: 1200px; height: 780px;
    display: flex; align-items: center; justify-content: center; gap: 40px;
  }
  .card {
    position: relative; width: 540px; height: 309px;
    border-radius: 6px; overflow: hidden;
    box-shadow: 0 10px 28px rgba(0,0,0,0.25);
  }
  .card--front { background: var(--card-black); }
  .card--back { background: var(--grill-dark); }
  .card-art { position: absolute; inset: 0; width: 100%; height: 100%; }

  .brand {
    position: absolute; display: flex; align-items: center; gap: 10px;
    color: var(--text-white); font-weight: 600; font-size: 34px; letter-spacing: 0.5px;
  }
  .brand-dot {
    width: 14px; height: 14px; border-radius: 50%; background: var(--accent-red);
  }
  .card--front .brand { left: 34px; top: 128px; }
  .card--back .brand { left: 50%; top: 112px; transform: translateX(-50%); font-size: 40px; }

  .tagline {
    position: absolute; right: 24px; top: 124px; width: 240px;
    color: var(--text-white); font-size: 14px; line-height: 1.35; text-align: left;
  }
  .web {
    position: absolute; color: var(--text-soft); font-size: 13px;
  }
  .card--front .web { right: 24px; top: 172px; width: 240px; }
  .card--back .web { left: 0; right: 0; top: 176px; text-align: center; font-size: 14px; }
</style>
</head>
<body>
<main class="sheet">

  <section class="card card--front" aria-label="Card front">
    <svg class="card-art" viewBox="0 0 540 309" aria-hidden="false">
      <defs>
        <linearGradient id="dishTop" x1="0" y1="0" x2="1" y2="1">
          <stop offset="0" stop-color="#d9d5a0"/>
          <stop offset="0.5" stop-color="#9bbd4f"/>
          <stop offset="1" stop-color="#7a4e34"/>
        </linearGradient>
        <linearGradient id="dishBottom" x1="0" y1="0" x2="1" y2="1">
          <stop offset="0" stop-color="#f2b48f"/>
          <stop offset="0.5" stop-color="#e0805a"/>
          <stop offset="1" stop-color="#f1e2cf"/>
        </linearGradient>
      </defs>
      <path d="M150 0 H540 V104 Q400 132 150 0 Z" fill="var(--accent-red)"/>
      <path role="img" aria-label="Photo of a grilled meat and pepper sandwich" d="M150 0 H540 V92 Q400 118 150 0 Z" fill="url(#dishTop)"/>
      <path d="M250 309 Q330 212 540 206 V309 Z" fill="var(--accent-red)"/>
      <path role="img" aria-label="Photo of a pepperoni pizza slice" d="M266 309 Q342 224 540 220 V309 Z" fill="url(#dishBottom)"/>
    </svg>
    <div class="brand"><span class="brand-dot"></span><span class="brand-name">PlateMarks</span></div>
    <p class="tagline">The Definitive guide to kosher dining for the Kosher consumer</p>
    <p class="web">http://restaurant.vintrello.com/</p>
  </section>

  <section class="card card--back" aria-label="Card back">
    <svg class="card-art" viewBox="0 0 540 309">
      <defs>
        <radialGradient id="grillShade" cx="0.5" cy="0.55" r="0.7">
          <stop offset="0" stop-color="var(--grill-mid)"/>
          <stop offset="1" stop-color="var(--grill-dark)"/>
        </radialGradient>
      </defs>
      <rect role="img" aria-label="Dark photo of meat and vegetables on a grill" width="540" height="309" fill="url(#grillShade)"/>
      <rect width="540" height="309" fill="rgba(0,0,0,0.35)"/>
    </svg>
    <div class="brand"><span class="brand-dot"></span><span class="brand-name">PlateMarks</span></div>
    <p class="web">http://restaurant.vintrello.com/</p>
  </section>

</main>
</body>
</html>
```